Tawny Bites menu + business card design

I want a menu design for my Food Truck.

I have attached the logo for it and my sliders will have different colors such as ( Black sliders, Red sliders and normal color) a picture will illustrates what I mean.

The menu should include:

Sliders:

Tawny Bite Single

Tawny Bites Meal

Fries:

Tawny Fries

Drinks:
Tawny Mojito

Water

BrisaPop

Desserts:

Charcoal cake

Target Market(s)

All

Industry/Entity Type

Business

Contact Information for Business Card

My theme is black and yellow like my logo

Colors

Designer to choose colors to be used in the design.

Requirements
Must have
• WhatsApp logo and the number for it is : +966507392048 " please dont squeeze the numbers".
• Instagram logo and my account is: TawnyBites
• Snapchat logo and my account is: TawnyBites
• Email logo and my email is: TheTawnyBites@postvale.com
Nice to have
• Circle design of the whole business card but it is not a must
• i will attach a picture.

```html
<!DOCTYPE html>
<html lang="en">
<head>
<meta charset="utf-8">
<title>Tawny Bites – Round Business Card</title>
<link rel="stylesheet" href="https://fonts.googleapis.com/css2?family=Fredoka:wght@500;700&display=swap">
<style>
  :root {
    --bg-light: #e09a48;
    --bg-mid: #dc8a35;
    --bg-deep: #e8681a;
    --card: #ffffff;
    --accent: #e8681a;
    --ink: #231f20;
    --shadow: rgba(120, 50, 0, 0.35);
  }
  * { margin: 0; padding: 0; box-sizing: border-box; }
  html, body {
    width: 1200px;
    height: 848px;
    overflow: hidden;
  }
  body {
    background: linear-gradient(100deg, var(--bg-light) 0%, var(--bg-mid) 50%, var(--bg-deep) 100%);
    font-family: "Fredoka", sans-serif;
  }
  .canvas {
    position: relative;
    width: 1200px;
    height: 848px;
  }
  .round-card {
    position: absolute;
    left: 396px;
    top: 242px;
    width: 408px;
    height: 408px;
    border-radius: 50%;
    background: var(--card);
    box-shadow: 0 6px 18px var(--shadow);
  }
  .rim-layer {
    position: absolute;
    left: 0;
    top: 0;
    width: 1200px;
    height: 848px;
  }
  .rim-text {
    font-family: "Fredoka", sans-serif;
    font-weight: 500;
    font-size: 15px;
    letter-spacing: 2.4px;
    fill: var(--accent);
    text-transform: uppercase;
  }
  .rim-icon {
    fill: none;
    stroke: var(--accent);
    stroke-width: 1.6;
    stroke-linejoin: round;
    stroke-linecap: round;
  }
  .brand-name {
    position: absolute;
    left: 396px;
    top: 242px;
    width: 408px;
    height: 408px;
    display: flex;
    flex-direction: column;
    align-items: center;
    justify-content: center;
    color: var(--ink);
    font-family: "Fredoka", sans-serif;
    font-weight: 700;
    font-size: 56px;
    line-height: 0.95;
    letter-spacing: 1px;
    text-transform: uppercase;
  }
</style>
</head>
<body>
<main class="canvas">
  <div class="round-card"></div>

  <div class="brand-name" aria-label="Tawny Bites">
    <span>Tawny</span>
    <span>Bites</span>
  </div>

  <svg class="rim-layer" viewBox="0 0 1200 848" xmlns="http://www.w3.org/2000/svg">
    <defs>
      <path id="rim-path" d="M 410,446 A 190 190 0 1 0 790,446 A 190 190 0 1 0 410,446"/>
    </defs>

    <text class="rim-text" text-anchor="middle">
      <textPath href="#rim-path" startOffset="99">@TawnyBites</textPath>
    </text>
    <text class="rim-text" text-anchor="middle">
      <textPath href="#rim-path" startOffset="298">TawnyBites</textPath>
    </text>
    <text class="rim-text" text-anchor="middle">
      <textPath href="#rim-path" startOffset="630">+966507392048</textPath>
    </text>
    <text class="rim-text" text-anchor="middle">
      <textPath href="#rim-path" startOffset="978">TheTawnyBites@postvale.com</textPath>
    </text>

    <!-- instagram marker -->
    <g class="rim-icon" transform="translate(416.4 457.6) rotate(86.4)">
      <circle cx="0" cy="0" r="5.5"/>
    </g>
    <!-- snapchat marker -->
    <g class="rim-icon" transform="translate(524.3 613.7) rotate(24.3)">
      <circle cx="0" cy="0" r="5.5"/>
    </g>
    <!-- phone icon -->
    <g class="rim-icon" transform="translate(772.7 509.5) rotate(-69.8)">
      <rect x="-4" y="-6.5" width="8" height="13" rx="1.6"/>
      <line x1="-1.2" y1="4" x2="1.2" y2="4"/>
    </g>
    <!-- email icon -->
    <g class="rim-icon" transform="translate(690.4 285.7) rotate(-150.6)">
      <rect x="-6.5" y="-4.5" width="13" height="9" rx="1"/>
      <polyline points="-6.5,-4.5 0,1 6.5,-4.5"/>
    </g>
  </svg>
</main>
</body>
</html>
```